Security based company delivering Ironwood Training to Law Enforcement Agencies Worldwide.

We need a Web design for a company doing business in Washington D.C. We deliver Ironwood Training to Law Enforcement Agencies throughout the world. Our focus is on Improvised Explosive Devices. We train Bomb Technicians and First Responders in all aspects relating to bombings and criminal incidents globally.
Updates

Reason: We have uploaded our logo. Thank you.

Target Market(s)

Military and Law Enforcement Personnel from around the world.

Industry/Entity Type

Business

Requirements
Should not have
• Do not include cartoon like characters.

```html
<!DOCTYPE html>
<html lang="en">
<head>
<meta charset="utf-8">
<title>Ironwood Training</title>
<link rel="stylesheet" href="https://fonts.googleapis.com/css2?family=PT+Sans+Narrow:wght@400;700&family=Lato:ital,wght@0,400;0,700;1,300;1,400;1,700&display=swap">
<style>
:root{
  --ink:#111;
  --muted:#8a8a8a;
  --body-text:#1a1a1a;
  --quote-text:#6a6a6a;
  --band-top:#f1f1f1;
  --band-bottom:#dcdcdc;
  --link-blue:#1f86c9;
  --btn-top:#e0623a;
  --btn-bottom:#b8361a;
  --footer:#78a6cc;
  --bar-top:#4d83b3;
  --bar-bottom:#2b4c66;
  --white:#fff;
}
*{margin:0;padding:0;box-sizing:border-box}
html,body{width:1200px;height:940px;overflow:hidden;background:#fff}
.page{position:relative;width:1200px;height:940px;font-family:"PT Sans Narrow",sans-serif;color:var(--ink)}

.intro-text{position:absolute;left:152px;top:-6px;width:340px;font-size:17px;line-height:18px;color:var(--muted)}
.intro-photo{position:absolute;left:580px;top:0;width:500px;height:74px;background:linear-gradient(180deg,#9a958c 0%,#c9b79a 55%,#b9a486 100%)}

.testimonials{position:absolute;left:0;top:166px;width:1200px;height:239px;background:linear-gradient(180deg,var(--band-top),var(--band-bottom))}
.quote-rule{position:absolute;left:0;top:130px;width:1200px;height:40px}
.testimonials h2{position:absolute;left:156px;top:44px;font-size:18px;font-weight:700;text-transform:uppercase}
.testimonials .lead{position:absolute;left:159px;top:83px;width:150px;font-size:17px;line-height:18px}
.avatar{position:absolute;left:397px;top:31px;width:94px;height:101px;background:#fff;border-radius:5px;box-shadow:0 2px 5px rgba(0,0,0,.25);padding:4px}
.avatar div{width:100%;height:100%;border-radius:3px;background:linear-gradient(160deg,#9cc6e4,#c8d6e0 50%,#7aa6cf)}
.quote{position:absolute;left:519px;top:36px;width:545px;font-family:Lato,sans-serif;font-style:italic;font-weight:300;font-size:13px;line-height:18px;color:var(--quote-text)}
.author{position:absolute;left:402px;top:158px;font-family:Lato,sans-serif;font-style:italic;font-weight:700;font-size:13px;color:var(--link-blue)}
.author span{color:var(--quote-text);font-weight:400}
.company{position:absolute;left:408px;top:176px;font-family:Lato,sans-serif;font-style:italic;font-weight:700;font-size:10px;color:#555}
.dots{position:absolute;left:1030px;top:170px;display:flex;gap:4px}
.dots i{width:11px;height:11px;border-radius:50%;background:#d2d2d2}
.dots i:first-child{background:#b5b5b5}

.news-photo{position:absolute;left:144px;top:446px;width:424px;height:283px;background:radial-gradient(circle at 55% 45%,#3a4a5a 0%,#1a2430 55%,#0c1016 100%)}
.news{position:absolute;left:623px;top:457px;width:440px}
.news h2{font-size:18px;font-weight:700;text-transform:uppercase}
.news h3{margin:24px 0 0 2px;font-size:22px;font-weight:700}
.news p{margin:14px 0 0 2px;font-size:17px;line-height:18px;color:var(--body-text)}
.btn{display:block;margin-top:13px;width:155px;height:38px;border-radius:4px;background:linear-gradient(180deg,var(--btn-top),var(--btn-bottom));box-shadow:0 1px 2px rgba(0,0,0,.4);color:var(--white);font-family:Lato,sans-serif;font-size:16px;line-height:38px;text-align:center;text-decoration:none;text-transform:uppercase}

.footer{position:absolute;left:0;top:813px;width:1200px;height:82px;background:var(--footer)}
.footer nav{position:absolute;left:144px;top:34px;font-size:22px;color:var(--white)}
.footer nav a{color:var(--white);text-decoration:none}
.social{position:absolute;left:906px;top:34px;display:flex;gap:2px}
.social span{width:27px;height:27px;border-radius:4px;background:#e9eef4;box-shadow:0 1px 2px rgba(0,0,0,.25)}
.copyright-bar{position:absolute;left:0;top:895px;width:1200px;height:45px;background:linear-gradient(180deg,var(--bar-top),var(--bar-bottom))}
.copyright-bar p{position:absolute;right:153px;top:13px;font-family:Lato,sans-serif;font-size:12px;color:var(--white)}
</style>
</head>
<body>
<div class="page">
  <p class="intro-text">do eiusmod tempor incididunt ut labore et dolore magna aliqua. Ut enim ad minim veniam, quis nostrud exercitation ullamco laboris nisi ut aliquip ex ea commodo consequat. Duis aute irure dolor in reprehenderit in voluptate velit esse cillum dolore eu fugiat nulla pariatur.</p>
  <div class="intro-photo" role="img" aria-label="Bomb technician kneeling beside equipment on a sandy street"></div>

  <section class="testimonials">
    <h2>Customer Testimonials</h2>
    <p class="lead">See what our customers are saying about Ironwood Training</p>
    <div class="avatar"><div role="img" aria-label="Portrait of a smiling customer"></div></div>
    <p class="quote">Sed ut perspiciatis unde omnis iste natus sit voluptatem accusantium doloremque laudantium, totam rem aperiam, eaque ipsa quae ab illo inventore veritatis et quasi . Sed ut perspiciatis unde omnis iste natus sit voluptatem accusantium. Sed ut perspiciatis unde omnis iste natus sit voluptatem accusantium doloremque laudantium, totam rem aperiam, eaque ipsa quae ab illo inventore veritatis et quasi . Sed ut perspiciatis unde omnis iste natus sit voluptatem accusantium.</p>
    <p class="author"><span>- </span>John Doe</p>
    <p class="company">Company Name</p>
    <div class="dots"><i></i><i></i><i></i></div>
  </section>

  <svg class="quote-rule" viewBox="0 0 1200 40" aria-hidden="true">
    <defs>
      <linearGradient id="rule" x1="0" x2="1">
        <stop offset="0" stop-color="#fff" stop-opacity="0"/>
        <stop offset=".5" stop-color="#fff"/>
        <stop offset="1" stop-color="#fff" stop-opacity="0"/>
      </linearGradient>
    </defs>
    <rect x="340" y="30" width="540" height="6" fill="url(#rule)"/>
    <circle cx="588" cy="28" r="20" fill="#fff" stroke="#e2e2e2"/>
    <text x="588" y="44" text-anchor="middle" font-family="Georgia,serif" font-size="34" font-weight="700" fill="#bdbdbd">&#8220;</text>
  </svg>

  <div class="news-photo" role="img" aria-label="Businessman touching a glowing interface of device icons"></div>
  <article class="news">
    <h2>Latest News</h2>
    <h3>Ut enim ad minim veniam, quis nostrud exercitation</h3>
    <p>Lorem ipsum dolor sit amet, consectetur adipiscing elit, sed do eiusmod tempor incididunt ut labore et dolore magna aliqua. Ut enim ad minim veniam, quis nostrud exercitation ullamco laboris nisi ut aliquip ex ea commodo consequat. Duis aute irure dolor in reprehenderit in voluptate velit esse cillum dolore eu fugiat nulla pariatur.</p>
    <a class="btn" href="#">Read More</a>
  </article>

  <footer class="footer">
    <nav><a href="#">About</a> | <a href="#">Services</a> | <a href="#">Contact</a></nav>
    <div class="social" aria-label="Social links">
      <span></span><span></span><span></span><span></span><span></span>
    </div>
  </footer>
  <div class="copyright-bar"><p>Copyright 2014. All Rights Reserved</p></div>
</div>
</body>
</html>
```